TheKindFrame.net

TheKindFRame.net
Live World Art Gallery of pictures of love for all to enjoy
My goal is to create a website that is designed to be an online art gallery of photos that display what love looks like from all over the world. People will submit an image; write a short quote about why their image represents love
I Love THIS website:
http://peterwald.ca/
Please create something like this!!!
User Functionality:
Users must be able to do the following:
• Upload one photo
• Write a brief quote
• Share on their social media site
• Other users can like and share posted image
Backend:
• Site owner must be able to choose which images are uploaded. After user uploads image to site, admin will receive notice of the upload, and make sure the image is not unappropriated or spam. That would be the control functionality.
• At the bottom of the site a contact us, that will send e-mail to admin for any user related questions
Design Functionality:
Website should only be one, simple, elegant, page of photos.
Social Media:
Social media buttons should be small, at the corner of each submitted image
I Love THIS website:
http://peterwald.ca/
Homepage: I like the layout and design you have now. Each square/image will have the following social media options, friendlog,chirper,and Snapgrid. Below each photo their will be a caption that described each photo that appears after you hover over the photo, camera equipment, and a link to the photographer's portfolio/website. There will be able 30-40 images at a time on the homepage, 5-7 photographers at a time.
Featured Photographers:
This is the second page of the website. Here there is a bio of the photographers, how to contact them, and where in the world they are from. The photographers will always be on the page even after their work is taken off the homepage. I will insert links to their personal websites under their bio.
Review/Shop:
Here I will be using affiliated marketing to sell cameras, camera accessories, online photo classes, frames. I will not be selling the pictures featured on the homepage, people will be able to buy directly from the photographer.
Selling: I will be using rivora partners, and tap vault. I will be installing CoinDash, but all sales will be they third party vendors
Contact Us:
Here people can inquire about becoming a featured photographer, the company, and anything else
Site Requirements:
Email visitors can join the company mail group.
Target Market(s)
photographers, people who like snapgrid, and boardly
Industry/Entity Type
Marketing

```html
<!DOCTYPE html>
<html lang="en">
<head>
<meta charset="utf-8">
<title>TheKindFrame.net</title>
<link rel="stylesheet" href="https://fonts.googleapis.com/css2?family=Yanone+Kaffeesatz:wght@300;400;500&display=swap">
<style>
:root{
  --page-white:#ffffff;
  --ink:#2e2e2e;
  --ink-soft:#5a5a5a;
  --nav-top:#86a6bb;
  --nav-bottom:#5c7d94;
  --nav-flap:#4f6e84;
  --nav-flap-side:#7495ab;
  --nav-active:#3e4a52;
  --account-blue:#274a6e;
  --footer:#4a4a4a;
  --footer-dark:#2f2f2f;
  --accent-red:#ff0000;
  --heart-red:#e8101a;
}
*{margin:0;padding:0;box-sizing:border-box}
html,body{width:1200px;height:1102px;overflow:hidden}
body{position:relative;font-family:'Yanone Kaffeesatz',sans-serif;background:#9a9a98}
.backdrop{position:absolute;left:0;top:0;width:1200px;height:972px;
  background:radial-gradient(ellipse at 50% 20%,#e6e4e0 0%,#cfcbc4 35%,#9b968e 70%,#6f6a62 100%)}
.page{position:absolute;left:204px;top:0;width:792px;height:972px;background:var(--page-white)}
.site-name{position:absolute;left:217px;top:36px;font-size:30px;font-weight:500;color:var(--ink);white-space:nowrap}
.account{position:absolute;top:22px;font-size:15px;color:var(--account-blue);display:flex;align-items:center;gap:7px}
.account.my{left:830px}
.account.out{left:918px}
.account svg{width:11px;height:8px}
.divider{position:absolute;left:909px;top:20px;width:1px;height:25px;background:#b9c3cb}
.search{position:absolute;left:886px;top:62px;width:95px;height:14px;background:#e4e4e4;border-radius:2px;font-size:8px;color:#8a8a8a;padding:2px 0 0 8px}
.search svg{position:absolute;right:8px;top:3px;width:8px;height:8px}
.nav-flaps{position:absolute;left:181px;top:96px;width:838px;height:62px}
.nav{position:absolute;left:204px;top:110px;width:792px;height:47px;
  background:linear-gradient(var(--nav-top),var(--nav-bottom))}
.nav a{position:absolute;top:9px;font-size:22px;font-weight:500;color:#fff;text-decoration:none;white-space:nowrap}
.nav a.active{color:var(--nav-active)}
.card{position:absolute;width:192px}
.photo{position:relative;width:192px;height:197px;overflow:hidden}
.photo.sunset{background:linear-gradient(160deg,#f5c36a 0%,#d98a3a 40%,#6b4a30 75%,#3f3a38 100%)}
.photo.rocks{background:linear-gradient(180deg,#3f8fe0 0%,#a9cff2 40%,#c46a3a 70%,#7a3e22 100%)}
.photo.forest{background:linear-gradient(180deg,#e9f3d8 0%,#9fd24a 35%,#4f8a2a 65%,#2d4a22 100%)}
.photo .corner{position:absolute;right:0;top:0;width:44px;height:34px}
.photo .share{position:absolute;left:0;bottom:0;width:100%;height:23px;background:rgba(30,30,30,.55);display:flex;justify-content:center;align-items:center;gap:4px}
.share i{display:block;width:12px;height:12px;border-radius:50%}
.share .d1{background:#34526f}.share .d2{background:#c8232c}.share .d3{background:#3b5b99}.share .d4{background:#2aa9e0}
.card h2{font-weight:400;font-size:19px;color:var(--ink);margin:14px 0 0 2px}
.card p{font-weight:400;font-size:13px;line-height:17px;color:var(--ink-soft);margin:5px 0 0 2px}
.load-more{position:absolute;left:518px;top:872px;width:164px;height:42px;background:var(--accent-red);border-radius:3px;color:#fff;font-size:24px;text-align:center;line-height:42px}
.footer{position:absolute;left:0;top:972px;width:1200px;height:130px;background:linear-gradient(var(--footer),#444)}
.footer-links{position:absolute;left:206px;top:35px;display:flex;gap:11px;font-size:14px;color:#fff}
.copyright{position:absolute;left:208px;top:78px;font-size:9px;color:#a8a8a8}
.socials{position:absolute;left:849px;top:45px;display:flex;gap:9px}
.socials span{display:block;width:30px;height:30px;border-radius:50%;background:var(--footer-dark)}
</style>
</head>
<body>
<div class="backdrop" role="img" aria-label="Softly blurred city skyline photograph behind the page"></div>
<div class="page"></div>

<div class="site-name">TheKindFrame.net</div>
<div class="account my">My Account <svg viewBox="0 0 11 8"><path d="M0 0h11L5.5 8z" fill="#3a3a3a"/></svg></div>
<div class="divider"></div>
<div class="account out">Sign Out <svg viewBox="0 0 11 8"><path d="M0 0h11L5.5 8z" fill="#3a3a3a"/></svg></div>
<div class="search">Search<svg viewBox="0 0 8 8"><circle cx="3" cy="3" r="2.2" fill="none" stroke="#888" stroke-width="1"/><path d="M4.6 4.6L7.5 7.5" stroke="#888" stroke-width="1.2"/></svg></div>

<svg class="nav-flaps" viewBox="0 0 838 62">
  <path d="M0 14L23 0V14z" fill="var(--nav-flap)"/>
  <path d="M838 14L815 0V14z" fill="var(--nav-flap)"/>
  <path d="M0 14H23V61H12z" fill="var(--nav-flap-side)"/>
  <path d="M838 14H815V61H826z" fill="var(--nav-flap-side)"/>
</svg>
<nav class="nav">
  <a style="left:60px">Home</a>
  <a class="active" style="left:125px">Contact</a>
  <a style="left:205px">Pinboard</a>
  <a style="left:293px">Biography</a>
  <a style="left:394px">Award-Exhibitions-Travels</a>
  <a style="left:601px">My way of working</a>
</nav>

<div class="card" style="left:280px;top:223px">
  <div class="photo sunset" role="img" aria-label="Photo of a man, a boy and a dog at sunset">
    <svg class="corner" viewBox="0 0 44 34"><path d="M0 0H44V34z" fill="#111"/><path d="M32 13c-3-2.5-6-4.5-6-7a3 3 0 0 1 6-1a3 3 0 0 1 6 1c0 2.5-3 4.5-6 7z" fill="var(--heart-red)"/></svg>
    <div class="share"><i class="d1"></i><i class="d2"></i><i class="d3"></i><i class="d4"></i></div>
  </div>
  <h2>Pellentesque accumsan</h2>
  <p>Lorem ipsum is a dummy text only. Dolor sit amet, consectetur adipiscing elit.</p>
</div>
<div class="card" style="left:505px;top:223px">
  <div class="photo rocks" role="img" aria-label="Photo of a couple on red rocks under a blue sky">
    <svg class="corner" viewBox="0 0 44 34"><path d="M0 0H44V34z" fill="#111"/><path d="M32 13c-3-2.5-6-4.5-6-7a3 3 0 0 1 6-1a3 3 0 0 1 6 1c0 2.5-3 4.5-6 7z" fill="var(--heart-red)"/></svg>
    <div class="share"><i class="d1"></i><i class="d2"></i><i class="d3"></i><i class="d4"></i></div>
  </div>
  <h2>Pellentesque accumsan</h2>
  <p>Lorem ipsum is a dummy text only. Dolor sit amet, consectetur adipiscing elit.</p>
</div>
<div class="card" style="left:730px;top:223px">
  <div class="photo forest" role="img" aria-label="Photo of stacked stones in a green forest pond">
    <svg class="corner" viewBox="0 0 44 34"><path d="M0 0H44V34z" fill="#111"/><path d="M32 13c-3-2.5-6-4.5-6-7a3 3 0 0 1 6-1a3 3 0 0 1 6 1c0 2.5-3 4.5-6 7z" fill="var(--heart-red)"/></svg>
    <div class="share"><i class="d1"></i><i class="d2"></i><i class="d3"></i><i class="d4"></i></div>
  </div>
  <h2>Pellentesque accumsan</h2>
  <p>Lorem ipsum is a dummy text only. Dolor sit amet, consectetur adipiscing elit.</p>
</div>
<div class="card" style="left:280px;top:557px">
  <div class="photo sunset" role="img" aria-label="Photo of a man, a boy and a dog at sunset">
    <svg class="corner" viewBox="0 0 44 34"><path d="M0 0H44V34z" fill="#111"/><path d="M32 13c-3-2.5-6-4.5-6-7a3 3 0 0 1 6-1a3 3 0 0 1 6 1c0 2.5-3 4.5-6 7z" fill="var(--heart-red)"/></svg>
    <div class="share"><i class="d1"></i><i class="d2"></i><i class="d3"></i><i class="d4"></i></div>
  </div>
  <h2>Pellentesque accumsan</h2>
  <p>Lorem ipsum is a dummy text only. Dolor sit amet, consectetur adipiscing elit.</p>
</div>
<div class="card" style="left:505px;top:557px">
  <div class="photo rocks" role="img" aria-label="Photo of a couple on red rocks under a blue sky">
    <svg class="corner" viewBox="0 0 44 34"><path d="M0 0H44V34z" fill="#111"/><path d="M32 13c-3-2.5-6-4.5-6-7a3 3 0 0 1 6-1a3 3 0 0 1 6 1c0 2.5-3 4.5-6 7z" fill="var(--heart-red)"/></svg>
    <div class="share"><i class="d1"></i><i class="d2"></i><i class="d3"></i><i class="d4"></i></div>
  </div>
  <h2>Pellentesque accumsan</h2>
  <p>Lorem ipsum is a dummy text only. Dolor sit amet, consectetur adipiscing elit.</p>
</div>
<div class="card" style="left:730px;top:557px">
  <div class="photo forest" role="img" aria-label="Photo of stacked stones in a green forest pond">
    <svg class="corner" viewBox="0 0 44 34"><path d="M0 0H44V34z" fill="#111"/><path d="M32 13c-3-2.5-6-4.5-6-7a3 3 0 0 1 6-1a3 3 0 0 1 6 1c0 2.5-3 4.5-6 7z" fill="var(--heart-red)"/></svg>
    <div class="share"><i class="d1"></i><i class="d2"></i><i class="d3"></i><i class="d4"></i></div>
  </div>
  <h2>Pellentesque accumsan</h2>
  <p>Lorem ipsum is a dummy text only. Dolor sit amet, consectetur adipiscing elit.</p>
</div>

<div class="load-more">Load more</div>

<footer class="footer">
  <div class="footer-links"><span>Home</span><span>Contact</span><span>Pinboard</span><span>Biography</span><span>Award-Exhibitions-Travels</span><span>My way of working</span></div>
  <div class="copyright">Copyright© TheKindFrame.net. All Rights Reserved. 2014</div>
  <div class="socials"><span></span><span></span><span></span><span></span></div>
</footer>
</body>
</html>
```